Postcard Design - Thanksgiving Card - Harvest Ridge Coils

Here are just a few of the heating and cooling products we offer:

• Steam Coils • Convector Coils
• Hot Water Coils • Re-Heat Coils
• Chilled Water Coils • Tube Bundles
• Direct Expansion (Evaporator) Coils • Shell & Tube Heat Exchangers
• Condensing Coils • Custom Coils to end user spec.’s

ENGINEERING - We can duplicate any existing equipment, even equipment that has been obsolete for years. Harvest Ridge personnel will come directly to your job site and match-up dimensions, materials, and performance - all free of charge. We can build from copper, aluminum, cupro-nickel, brass, and more. Heat exchangers and tube bundles can be replaced & warranted as new with great savings; this includes Lark & Thimble, Morrow-Dennick, Vexo, and others. We also make engineering recommendations and suggestions regarding the correct ways to replace equipment or methods of increasing the life expectancy of equipment. We will help solve your HVAC problems, not duplicate them.

Industry/Entity Type

Hvac

```html
<!DOCTYPE html>
<html lang="en">
<head>
<meta charset="utf-8">
<title>Harvest Ridge Coils – Thanksgiving Postcard</title>
<link href="https://fonts.googleapis.com/css2?family=Lato:ital,wght@1,300&family=Montserrat:wght@400;600;700&family=Great+Vibes&family=Oswald:wght@500&display=swap" rel="stylesheet">
<style>
  :root {
    --stage: #000000;
    --card: #ffffff;
    --brown: #6b2a1e;
    --ink: #3a3a3a;
    --quote: #555555;
    --copper-dark: #6e3a22;
    --copper: #b06a45;
    --copper-light: #e2b79c;
    --steel: #b9b9bb;
    --autumn-warm: #e7c9a5;
    --autumn-soft: #f6ede1;
    --autumn-gold: #e9d79a;
  }
  * { margin: 0; padding: 0; box-sizing: border-box; }
  html, body { width: 783px; height: 1200px; overflow: hidden; background: var(--stage); }
  .canvas { position: relative; width: 783px; height: 1200px; }

  .card { position: absolute; left: 46px; width: 691px; height: 535px; background: var(--card); overflow: hidden; }
  .card--front { top: 57px; background: linear-gradient(180deg, #ffffff 60%, #f2f2f2 100%); }
  .card--back { top: 617px; }

  .coil-photo {
    position: absolute; inset: 0;
    clip-path: polygon(0 0, 100% 0, 100% 12%, 0 57%);
    background: linear-gradient(160deg, var(--copper-dark) 0%, var(--copper) 35%, var(--copper-light) 62%, var(--steel) 100%);
  }

  .quote {
    position: absolute; left: 290px; top: 236px; width: 380px;
    font-family: 'Lato', sans-serif; font-style: italic; font-weight: 300;
    font-size: 17.5px; line-height: 25.7px; color: var(--quote); text-align: center; letter-spacing: -0.5px;
    white-space: nowrap;
  }
  .signature {
    position: absolute; top: 370px;
    font-family: 'Great Vibes', cursive; font-size: 32px; color: var(--brown);
  }
  .signature--first { left: 378px; }
  .signature--second { left: 528px; }

  .brand { position: absolute; text-align: center; }
  .brand__name {
    display: flex; align-items: center; justify-content: center; gap: 7px;
    font-family: 'Oswald', sans-serif; font-weight: 500; font-size: 22px; line-height: 30px;
    color: #111111; text-transform: uppercase; letter-spacing: 0.5px;
  }
  .brand__mark { width: 12px; height: 12px; background: #111111; }
  .brand__tagline {
    margin-top: 4px; font-family: 'Oswald', sans-serif; font-weight: 500;
    font-size: 12px; line-height: 15px; color: #111111; letter-spacing: 0.2px;
  }
  .card--front .brand { left: 18px; top: 360px; width: 240px; }

  .contact-line {
    position: absolute; left: 0; right: 0; top: 432px; text-align: center;
    font-family: 'Montserrat', sans-serif; font-size: 14px; line-height: 18px; color: var(--ink);
  }
  .contact-line strong { font-weight: 700; color: #222; }
  .contact-line .sep { margin: 0 6px; }
  .rule { position: absolute; left: 0; right: 0; top: 458px; height: 2px; background: var(--brown); }
  .services {
    position: absolute; left: 0; right: 0; top: 466px; text-align: center;
    font-family: 'Montserrat', sans-serif; font-size: 12.6px; line-height: 16.5px; color: var(--ink);
  }

  .leaf-backdrop {
    position: absolute; inset: 0;
    background:
      radial-gradient(ellipse 70% 80% at 22% 38%, var(--autumn-warm) 0%, rgba(231,201,165,0.4) 45%, transparent 75%),
      radial-gradient(ellipse 50% 40% at 85% 8%, var(--autumn-gold) 0%, transparent 70%),
      linear-gradient(120deg, #e8cfb0 0%, var(--autumn-soft) 55%, #fbf7f1 100%);
  }
  .return-address {
    position: absolute; left: 68px; top: 46px; width: 200px; text-align: center;
    font-family: 'Montserrat', sans-serif; font-size: 14px; line-height: 17px; color: var(--ink);
  }
  .leaf-art {
    position: absolute; left: 145px; top: 127px; width: 96px; height: 60px;
    border-radius: 50%;
    background: linear-gradient(110deg, #e3ddd4 0%, #d9a25a 60%, #c98a3e 100%);
  }
  .greeting {
    position: absolute; left: 40px; top: 186px; width: 300px;
    font-family: 'Great Vibes', cursive; font-weight: 400; color: var(--brown); line-height: 54px;
  }
  .greeting__line { display: block; font-size: 58px; }
  .greeting__line--first { padding-left: 66px; }
  .greeting__line--second { padding-left: 8px; }
  .card--back .brand { left: 53px; top: 378px; width: 230px; }
  .serving-band {
    position: absolute; left: 77px; top: 439px; width: 182px; height: 21px;
    background: var(--brown); color: #fff; text-align: center;
    font-family: 'Montserrat', sans-serif; font-weight: 600; font-size: 14.5px; line-height: 21px;
  }
  .back-phone {
    position: absolute; left: 68px; top: 463px; width: 200px; text-align: center;
    font-family: 'Montserrat', sans-serif; font-weight: 700; font-size: 21px; line-height: 26px; color: #222;
  }
  .back-email {
    position: absolute; left: 68px; top: 489px; width: 200px; text-align: center;
    font-family: 'Montserrat', sans-serif; font-size: 13.5px; line-height: 17px; color: var(--ink);
  }
</style>
</head>
<body>
<main class="canvas">

  <section class="card card--front">
    <div class="coil-photo" role="img" aria-label="Close-up photograph of copper coil return bends on a heat exchanger header"></div>

    <p class="quote">“It is the time of Year for remembering everything<br>that makes us grateful. That is why we want to<br>express our appreciation for your confidence in our<br>firm to assist you on your jobsite or at your facility<br>to solve a coil or heat exchanger problem.”</p>
    <span class="signature signature--first">Dale</span>
    <span class="signature signature--second">Russ</span>

    <div class="brand">
      <div class="brand__name"><span class="brand__mark"></span>Harvest Ridge Coils</div>
      <div class="brand__tagline">HVACR COILS • HEAT EXCHANGERS</div>
    </div>

    <p class="contact-line">Serving all of Michigan<span class="sep">|</span><strong>888-555-0142</strong><span class="sep">|</span>coilguy@harvestmail.net</p>
    <div class="rule"></div>
    <p class="services">
      • Steam Coils • Hot Water Coils • Chilled Water Coils • Condensing Coils<br>
      • Direct Expansion (Evaporator) Coils • Convector Coils • Re-Heat Coils • Tube Bundles<br>
      • Shell &amp; Tube Heat Exchangers • Custom Coils to end user spec.’s
    </p>
  </section>

  <section class="card card--back">
    <div class="leaf-backdrop" role="img" aria-label="Soft-focus photograph of an autumn maple leaf in warm peach and gold tones"></div>

    <p class="return-address">Dale Merrow &amp; Russ Holden<br>P.O. Box 718<br>Ashford, MI 48099</p>

    <div class="leaf-art" role="img" aria-label="Small illustration of three autumn leaves"></div>

    <h1 class="greeting">
      <span class="greeting__line greeting__line--first">Happy</span>
      <span class="greeting__line greeting__line--second">Thanksgiving!</span>
    </h1>

    <div class="brand">
      <div class="brand__name"><span class="brand__mark"></span>Harvest Ridge Coils</div>
      <div class="brand__tagline">HVACR COILS • HEAT EXCHANGERS</div>
    </div>

    <div class="serving-band">Serving all of Michigan</div>
    <p class="back-phone">888-555-0142</p>
    <p class="back-email">coilguy@harvestmail.net</p>
  </section>

</main>
</body>
</html>
```